Judicial Invitation for Political Campaign

I need an invitation template for a judicial fundraiser for political candidtate in Texas.  The invitation will be a flat size of 10 x 7 and a folded size of 5 x 7.  Can fold horizontal or vertical.  Invitation must incorporate the candidate's logo in the design.
I have multiple candidates so this could be an on-going project.  I have attached the various candidate logos so you may choose and work with whatever logo you prefer...
the inside panels of the invitation will have various text added as the events get finalized so right now I just need any design that you would like to add to the inside.  It should be light enough or framed so that there is sufficient room at the top or right side for a large list of contributors and the bottom or left side will have information about the event.
Please feel free to email if you need clarification.

Updates
Logos have been uploaded.  Please use only one logo per invitation.  Each candidate will have separate events.

Industry/Entity Type
Political
Look and feel

```html
<!DOCTYPE html>
<html lang="en">
<head>
<meta charset="utf-8">
<title>Keep Judge Helen Marsh – Fundraiser Invitation</title>
<link href="https://fonts.googleapis.com/css2?family=Open+Sans:wght@400;600;700;800&display=swap" rel="stylesheet">
<style>
  :root {
    --navy: #2b4f96;
    --red: #e2352f;
    --ink: #1f1f1f;
    --paper: #ffffff;
    --backdrop: #ecebe8;
    --fold: #d6d6d6;
    --flag-red: rgba(226, 53, 47, 0.10);
    --flag-blue: rgba(43, 79, 150, 0.08);
  }
  * { margin: 0; padding: 0; box-sizing: border-box; }
  html, body { width: 975px; height: 1200px; overflow: hidden; }
  body {
    background: var(--backdrop);
    font-family: "Open Sans", Arial, sans-serif;
    color: var(--ink);
    position: relative;
  }
  .sheet {
    position: absolute;
    left: 105px;
    width: 765px;
    height: 533px;
    background: var(--paper);
    box-shadow: 0 2px 6px rgba(0,0,0,0.18);
    overflow: hidden;
  }
  .sheet--outside { top: 62px; }
  .sheet--inside { top: 618px; }
  .sheet__band { position: absolute; left: 0; right: 0; top: 0; height: 21px; background: var(--navy); }
  .sheet__band-rule { position: absolute; left: 0; right: 0; top: 24px; height: 3px; background: var(--red); }
  .sheet__foot-rule { position: absolute; left: 0; right: 0; bottom: 12px; height: 3px; background: var(--navy); }
  .sheet__foot-rule--red { bottom: 7px; height: 2px; background: var(--red); }
  .sheet__fold { position: absolute; top: 21px; bottom: 0; left: 382px; width: 1px; background: var(--fold); }
  .flag-wash { position: absolute; }
  .flag-wash--back {
    left: 0; top: 195px; width: 382px; height: 320px;
    background: linear-gradient(160deg, var(--flag-red) 0%, var(--flag-blue) 55%, rgba(255,255,255,0) 100%);
  }
  .flag-wash--front {
    left: 382px; top: 285px; width: 383px; height: 230px;
    background: linear-gradient(170deg, var(--flag-red) 0%, rgba(255,255,255,0) 70%);
  }
  .flag-wash--inside {
    left: 382px; top: 420px; width: 383px; height: 95px;
    background: linear-gradient(175deg, var(--flag-red) 0%, rgba(255,255,255,0) 80%);
  }
  .candidate-name {
    position: absolute;
    color: var(--navy);
    font-weight: 800;
    text-transform: uppercase;
    line-height: 1.05;
    display: flex; align-items: center; gap: 6px;
  }
  .candidate-name__mark { width: 10px; height: 10px; background: var(--navy); flex: none; }
  .candidate-name--small { left: 40px; top: 48px; font-size: 13px; width: 110px; }
  .candidate-name--large { left: 492px; top: 44px; font-size: 24px; width: 200px; justify-content: center; text-align: center; }
  .candidate-name--large .candidate-name__mark { width: 14px; height: 14px; }
  .portrait {
    position: absolute; left: 445px; top: 145px; width: 255px; height: 170px;
    background: linear-gradient(90deg, #6b5a47 0%, #3b3430 45%, #8a7a66 100%);
  }
  .event-title {
    position: absolute; left: 382px; right: 0; top: 350px;
    text-align: center; color: var(--navy); font-weight: 700; font-size: 15px;
  }
  .intro {
    position: absolute; left: 420px; width: 309px; top: 428px;
    font-size: 8.6px; line-height: 15px; text-align: justify;
  }
  .contributors { position: absolute; left: 400px; top: 40px; }
  .contributors__heading { color: var(--navy); font-weight: 700; font-size: 14px; margin-bottom: 2px; }
  .contributors__list { list-style: none; font-size: 12px; line-height: 17px; }
  .callout {
    position: absolute; left: 400px; top: 128px;
    color: var(--red); font-weight: 700; font-size: 11px; line-height: 18px; text-transform: uppercase;
  }
  .venue-photo {
    position: absolute; top: 197px; width: 166px; height: 115px;
    border: 2px solid var(--navy); border-radius: 5px;
  }
  .venue-photo--hall { left: 400px; background: linear-gradient(180deg, #7a5a36 0%, #c9a66e 50%, #e8e1d4 100%); }
  .venue-photo--tables { left: 581px; background: linear-gradient(180deg, #b99b63 0%, #e7ddc9 50%, #b2232a 100%); }
  .details-copy {
    position: absolute; left: 400px; width: 330px; top: 340px;
    font-size: 8.6px; line-height: 14px;
  }
  .proceeds {
    position: absolute; left: 400px; top: 424px;
    color: var(--navy); font-weight: 700; font-size: 9.5px;
  }
  .event-info, .ticket-info {
    position: absolute; top: 453px; font-size: 9.5px; font-weight: 700; line-height: 13px;
  }
  .event-info { left: 400px; }
  .event-info p + p { margin-top: 5px; }
  .ticket-info { left: 594px; line-height: 14px; }
</style>
</head>
<body>

<section class="sheet sheet--outside">
  <div class="sheet__band"></div>
  <div class="sheet__band-rule"></div>
  <div class="flag-wash flag-wash--back" role="img" aria-label="Faint brushed American flag backdrop"></div>
  <div class="flag-wash flag-wash--front" role="img" aria-label="Faint brushed American flag backdrop"></div>
  <div class="sheet__fold"></div>

  <div class="candidate-name candidate-name--small"><span class="candidate-name__mark"></span><span>Keep Judge Helen Marsh</span></div>
  <div class="candidate-name candidate-name--large"><span class="candidate-name__mark"></span><span>Keep Judge Helen Marsh</span></div>

  <div class="portrait" role="img" aria-label="Portrait photo of the candidate in a dark suit"></div>
  <h1 class="event-title">2014 POLITICAL ACTION FUNDRAISER</h1>
  <p class="intro">Lorem Ipsum Dolor Sit Amet, Consectetuer Adipiscing Elit, Sed Diam Nonummy Nibh Euismod Tincidunt Ut Laoreet Dolore Magna Aliquam Erat Volutpat. Ut Wisi Enim Ad Minim Veniam, Quis Nostrud Exerci Tation Ullamcorper Suscipit Lobortis Nisl Ut Aliquip Ex Ea Commodo Consequat.</p>

  <div class="sheet__foot-rule"></div>
  <div class="sheet__foot-rule sheet__foot-rule--red"></div>
</section>

<section class="sheet sheet--inside">
  <div class="sheet__band"></div>
  <div class="sheet__band-rule"></div>
  <div class="flag-wash flag-wash--inside" role="img" aria-label="Faint brushed American flag backdrop"></div>
  <div class="sheet__fold"></div>

  <div class="contributors">
    <h2 class="contributors__heading">CONTRIBUTORS</h2>
    <ul class="contributors__list">
      <li>Lorem ipsum</li>
      <li>Lorem ipsum</li>
      <li>Lorem ipsum</li>
    </ul>
  </div>

  <p class="callout">Come out &amp; meet the your elected officicals<br>and candidates for the&nbsp; upcoming primary election</p>

  <div class="venue-photo venue-photo--hall" role="img" aria-label="Photo of a banquet hall with chandeliers and round tables"></div>
  <div class="venue-photo venue-photo--tables" role="img" aria-label="Photo of red-draped auction tables in a hall"></div>

  <p class="details-copy">Lorem ipsum dolor sit amet, consectetuer adipiscing elit, sed diam nonummy nibh euismod tincidunt ut laoreet dolore magna aliquam erat volutpat. Ut wisi enim ad minim veniam, quis nostrud exerci tation ullamcorper suscipit lobortis nisl ut aliquip ex ea commodo consequat.</p>

  <p class="proceeds">All Proceeds Go to Local 1234,Lorem Political Action Fund</p>

  <div class="event-info">
    <p>Date :Saturday, April 18, 2014<br>Time: 12 Noon - 18:00 pm</p>
    <p>Place: Local 1234 Union Hall<br>740 Elm Street</p>
  </div>
  <div class="ticket-info">
    <p>For&nbsp; Ticket Please Contact<br>Lorem Ispum&nbsp; P: 123-456-7890<br>Lorem&nbsp; P: 123-456-7890<br>Lorem&nbsp; P: 123-456-7890</p>
  </div>

  <div class="sheet__foot-rule"></div>
  <div class="sheet__foot-rule sheet__foot-rule--red"></div>
</section>

</body>
</html>
```